Lantern on The Hill Business Card Design

Simple 2 sided card ideally based around a zen garden approach (larger stone in a sand combed garden), but not essential.
Business is Project Management, IT Consultancy, Business Analysis.
Initially one person, however others may join the business so a unique logo would be preferred that encapsulates the approach of one pebble dropping in water causing many ripples. Potentially based around a zen garden, but not essential.
Clean and tidy, double sided, glossy, interesting and unique.
Company Name and contact details on one side (with the ability to replace the name, telephone and email address for more staff):
Lantern on The Hill Ltd
Derek Hollis
077 5182 6271
derek@lanternonthehill-mail.com
Company name and offering on the other:
Lantern on The Hill Ltd
Project Management
Business Analysis
IT Consultancy
Interesting looking font, nice colours, not too many, but simple, effective and eye catching.
Potential Image either as a background or to the left/ right. Replicated on the rear of the card.
Design once approved and complete to be the sole property of Lantern on The Hill Ltd.
No requirement for Twitter, Facebook or Linked in details on any design
Lantern on The Hill
Derek Hollis
077 5182 6271
Project Management
Business Analysis
IT Consultancy

```html
<!DOCTYPE html>
<html lang="en">
<head>
<meta charset="utf-8">
<title>Lantern on The Hill — Business Card</title>
<link rel="stylesheet" href="https://fonts.googleapis.com/css2?family=Open+Sans:wght@300;400;600;700;800&display=swap">
<style>
  :root {
    --page-bg: #e9ebee;
    --brand-blue: #1a7fb8;
    --brand-blue-dark: #12628f;
    --brand-blue-light: #2a97cf;
    --ink-blue: #1d6fa6;
    --paper: #ffffff;
    --sand-light: #e8e0d2;
    --sand-mid: #c9bca6;
    --sand-dark: #9c8d76;
    --stone: #efebe4;
  }
  * { box-sizing: border-box; margin: 0; padding: 0; }
  html, body {
    width: 1200px; height: 900px; overflow: hidden;
    background: var(--page-bg);
    font-family: "Open Sans", Verdana, sans-serif;
  }
  .canvas {
    position: relative; width: 1200px; height: 900px;
  }
  .card {
    position: absolute; left: 260px; width: 680px; height: 388px;
    border-radius: 10px; overflow: hidden;
    box-shadow: 0 10px 30px rgba(0,0,0,.18);
  }
  .card--back { top: 42px; background: linear-gradient(160deg, var(--brand-blue-light), var(--brand-blue) 55%, var(--brand-blue-dark)); }
  .card--front { top: 470px; }

  /* Back */
  .brand-mark {
    position: absolute; left: 150px; top: 36px;
    writing-mode: vertical-rl;
    color: var(--paper); font-weight: 700; font-size: 34px; line-height: 1.05;
    letter-spacing: .5px;
  }
  .offer-panel {
    position: absolute; left: 262px; right: 0; top: 40px; height: 178px;
    background: var(--paper);
    padding: 40px 0 0 56px;
  }
  .offer-list { list-style: none; }
  .offer-list li {
    color: var(--ink-blue); font-size: 22px; font-weight: 400; line-height: 34px;
  }

  /* Front */
  .scene-photo {
    position: absolute; inset: 0;
    background:
      radial-gradient(ellipse 150px 190px at 78% 58%, var(--stone) 0%, #ddd5c8 55%, transparent 75%),
      linear-gradient(180deg, var(--sand-light), var(--sand-mid) 60%, var(--sand-dark));
  }
  .name-band {
    position: absolute; left: 0; right: 0; top: 26px; height: 74px;
    background: linear-gradient(180deg, var(--brand-blue-light), var(--brand-blue));
    color: var(--paper);
    font-weight: 300; font-size: 44px; letter-spacing: 1.5px;
    display: flex; align-items: center; padding-left: 38px;
  }
  .name-band__pointer {
    position: absolute; left: 92px; bottom: -20px;
  }
  .contact {
    position: absolute; left: 38px; top: 160px;
  }
  .contact__name {
    color: var(--ink-blue); font-weight: 800; font-size: 42px;
    -webkit-text-stroke: 1px var(--paper);
    text-shadow: 0 0 6px var(--paper), 0 0 3px var(--paper);
    margin-bottom: 22px;
  }
  .contact__line {
    color: var(--ink-blue); font-size: 25px; font-weight: 400; line-height: 32px;
    text-shadow: 0 0 4px rgba(255,255,255,.7);
  }
</style>
</head>
<body>
<main class="canvas">

  <section class="card card--back" aria-label="Card reverse">
    <div class="brand-mark">Lantern on<br>The Hill</div>
    <div class="offer-panel">
      <ul class="offer-list">
        <li>Project Management</li>
        <li>Business Analysis</li>
        <li>IT Consultancy</li>
      </ul>
    </div>
  </section>

  <section class="card card--front" aria-label="Card front">
    <div class="scene-photo" role="img" aria-label="Photograph of three stacked smooth stones on a raked sand zen garden"></div>
    <div class="name-band">
      Lantern on The Hill
      <svg class="name-band__pointer" width="28" height="20" viewBox="0 0 28 20" aria-hidden="true">
        <polygon points="0,0 28,0 0,20" fill="#1a7fb8"/>
      </svg>
    </div>
    <div class="contact">
      <p class="contact__name">Derek Hollis</p>
      <p class="contact__line">077 5182 6271</p>
      <p class="contact__line">derek@lanternonthehill-mail.com</p>
    </div>
  </section>

</main>
</body>
</html>
```